Front/Back Product Label for "Tidewell Deck Cleaner" 1GAL

Overview
We have a boat deck cleaning product packaged in a one gallon container that requires two labels. The attached PowerPoint files provides the background and content. We need one label for the front side of the container (Slide 2) and one label for the back side of the container (Slide 3).
Container Size
1 Gallon. See Slide 4 for the label dimensions.
Design
Slide Nos. 2-3 are examples of design and content. We are looking for a professional design that has a nautical theme fitting for the product use.
Design Files
We do have the Marlowe Hullcraft logo design files. Other boat deck photos are also available if needed.
Target Market(s)
Boat and yacht owners, marinas and boat yards.
Look and feel
Each slider illustrates characteristics of the customer's brand and the style your logo design should communicate.

```html
<!DOCTYPE html>
<html lang="en">
<head>
<meta charset="utf-8">
<title>Tidewell Deck Cleaner – Front Label</title>
<link href="https://fonts.googleapis.com/css2?family=Big+Shoulders+Display:wght@300&family=Montserrat:wght@600;700;800&family=Open+Sans+Condensed:wght@700&family=Open+Sans:wght@700&display=swap" rel="stylesheet">
<style>
  :root {
    --page: #f1f1f1;
    --navy: #0b2350;
    --navy-deep: #071a3e;
    --navy-light: #143467;
    --white: #ffffff;
    --sky-warm: #e9dcc2;
    --sky-cool: #b9c4cf;
    --sea: #3c5069;
    --sea-deep: #243348;
    --badge: #e8ecf3;
  }
  html, body {
    margin: 0;
    width: 1200px;
    height: 1132px;
    overflow: hidden;
    background: var(--page);
  }
  .label {
    position: absolute;
    left: 50px;
    top: 70px;
    width: 1100px;
    height: 993px;
    background: linear-gradient(90deg, var(--navy-deep), var(--navy) 50%, var(--navy-deep));
    color: var(--white);
    overflow: hidden;
    font-family: "Montserrat", sans-serif;
  }
  .brand-header {
    position: absolute;
    inset: 0 0 auto 0;
    height: 368px;
  }
  .established {
    position: absolute;
    left: 45px;
    top: 150px;
    display: flex;
    align-items: center;
    gap: 18px;
    font-size: 17px;
    font-weight: 600;
    letter-spacing: 1px;
  }
  .established .mark {
    width: 44px;
    height: 44px;
    border: 3px solid var(--white);
    border-radius: 50%;
    box-sizing: border-box;
  }
  .brand-name {
    position: absolute;
    left: 293px;
    top: 40px;
    width: 760px;
    margin: 0;
    font-family: "Big Shoulders Display", sans-serif;
    font-weight: 300;
    font-size: 238px;
    line-height: 1;
    letter-spacing: 34px;
    text-align: center;
  }
  .brand-sub {
    position: absolute;
    left: 293px;
    top: 255px;
    width: 760px;
    text-align: center;
    font-size: 68px;
    font-weight: 600;
    letter-spacing: 11px;
    line-height: 1;
  }
  .deck-scene {
    position: absolute;
    left: 0;
    top: 368px;
    width: 1100px;
    height: 352px;
    background:
      linear-gradient(180deg, var(--navy-deep) 0%, transparent 4%, transparent 94%, var(--navy) 100%),
      linear-gradient(180deg, var(--sky-cool) 0%, var(--sky-warm) 30%, #d8d2c6 46%, var(--sea) 50%, var(--sea-deep) 100%);
  }
  .product-name {
    position: absolute;
    left: 42px;
    top: 782px;
    margin: 0;
    font-family: "Open Sans", sans-serif;
    font-weight: 700;
    font-size: 50px;
    line-height: 1;
    letter-spacing: -1px;
  }
  .product-type {
    position: absolute;
    left: 44px;
    top: 898px;
    font-family: "Open Sans Condensed", "Open Sans", sans-serif;
    font-weight: 700;
    font-size: 28px;
    letter-spacing: -0.5px;
  }
  .quality-seal {
    position: absolute;
    left: 369px;
    top: 767px;
    width: 130px;
    height: 130px;
    border-radius: 50%;
    background: var(--badge);
  }
  .volume {
    position: absolute;
    left: 335px;
    top: 932px;
    font-size: 31px;
    font-weight: 700;
    letter-spacing: 0.5px;
  }
  .features {
    position: absolute;
    left: 604px;
    top: 760px;
    margin: 0;
    padding: 0;
    list-style: none;
    font-size: 27px;
    font-weight: 700;
    line-height: 29px;
    letter-spacing: 0.6px;
  }
  .features li::before { content: "•"; }
  .caution {
    position: absolute;
    right: 22px;
    top: 951px;
    display: flex;
    align-items: center;
    gap: 5px;
    font-size: 12px;
    font-weight: 800;
  }
</style>
</head>
<body>
  <section class="label">
    <header class="brand-header">
      <div class="established"><span>EST.</span><span class="mark"></span><span>2019</span></div>
      <h1 class="brand-name">MARLOWE</h1>
      <div class="brand-sub">HULLCRAFT</div>
    </header>

    <div class="deck-scene" role="img" aria-label="Photo of a white sailboat deck under sail on open sea at sunset"></div>

    <h2 class="product-name">TIDEWELL</h2>
    <div class="product-type">DECK CLEANER</div>

    <div class="quality-seal" aria-hidden="true"></div>
    <div class="volume">1 GAL (3.78L</div>

    <ul class="features">
      <li>Neutral pH 7</li>
      <li>Safe For Synthetic Teak Decks</li>
      <li>Safe for hard surface finishes.</li>
      <li>Concentrate</li>
      <li>No Dyes</li>
      <li>No Harsh Acids &amp; Alkalis</li>
    </ul>

    <div class="caution">
      <svg width="16" height="16" viewBox="0 0 16 16" aria-hidden="true">
        <path d="M8 1 L15 8 L8 15 L1 8 Z" fill="none" stroke="#fff" stroke-width="1.4"/>
        <path d="M8 4.5 V9.5 M8 11 V12" stroke="#fff" stroke-width="1.6"/>
      </svg>
      <span>CAUTION: AVOID EYE CONTACT</span>
    </div>
  </section>
</body>
</html>
```